Business Card Design Project

We need a business card design for our company kB7 s.r.o. The company is based in Slovakia and selling massage, yoga and meditation accessories online and offline. At the place where the offices are, we have a yoga studio, massage room, show room and shop as well. We will give the business card for customers who visit our shop or show room personally and for the new suppliers of demanded products we are visiting in the future.
I would like to have:
- small logo and datas on one side
- big logo and our main e-shops on the other side:
- www.pohodlnelavice.sk
- www.relaxnipultiky.cz
Datas:
Peter Kolar, MSc. / CEO
kB7 s.r.o.
Borovicová 742/3
938 05 Dunajská Streda
Slovak republic (Slovakia)
Office tel.: +421 (0) 917 604 382
Private tel.: +421 (0) 911 758 026
E-mail: info@kb7.sk
Web: www.kb7.sk
It is up to you if you use graphics emphasizing our profile or leave it simple and modern without pics. Looking forward to receiving your designs! Thank You!

```html
<!DOCTYPE html>
<html lang="sk">
<head>
<meta charset="utf-8">
<title>kB7 s.r.o. – business card</title>
<link href="https://fonts.googleapis.com/css2?family=Exo+2:wght@400;500;600;700&display=swap" rel="stylesheet">
<style>
  :root {
    --orange: #f0711a;
    --slate: #38424e;
    --ink: #2b2f36;
    --grey: #6b6f75;
    --paper: #ffffff;
    --backdrop: #e9e6e2;
  }
  * { box-sizing: border-box; margin: 0; padding: 0; }
  html, body { width: 1200px; height: 900px; overflow: hidden; }
  body {
    background: var(--backdrop);
    font-family: "Exo 2", sans-serif;
    color: var(--ink);
    position: relative;
  }
  .card {
    position: absolute;
    left: 300px;
    width: 600px;
    height: 333px;
    box-shadow: 0 6px 18px rgba(0,0,0,0.18);
  }
  /* front */
  .card-front { top: 97px; background: var(--orange); }
  .brand-large {
    position: absolute;
    left: 50%; top: 96px;
    transform: translateX(-50%);
    display: flex; align-items: center; gap: 14px;
  }
  .brand-large .brand-dot { width: 34px; height: 34px; border-radius: 50%; background: var(--paper); }
  .brand-large .brand-name { font-size: 96px; font-weight: 700; color: var(--slate); line-height: 1; }
  .eshop {
    position: absolute;
    color: var(--paper);
    font-size: 17px; font-weight: 600;
    letter-spacing: 0.3px;
  }
  .eshop-sk { left: 36px; bottom: 26px; }
  .eshop-cz { right: 36px; bottom: 96px; }

  /* back */
  .card-back { top: 470px; background: var(--paper); }
  .brand-small {
    position: absolute; left: 44px; top: 96px;
    display: flex; align-items: center; gap: 8px;
  }
  .brand-small .brand-dot { width: 18px; height: 18px; border-radius: 50%; background: var(--orange); }
  .brand-small .brand-name { font-size: 56px; font-weight: 700; color: var(--slate); line-height: 1; }
  .holder { position: absolute; right: 36px; top: 24px; text-align: right; }
  .holder-name { color: var(--orange); font-size: 30px; font-weight: 500; letter-spacing: 1px; line-height: 1.05; }
  .holder-title { color: var(--grey); font-size: 15px; }
  .address {
    position: absolute; right: 36px; top: 100px;
    text-align: right; font-size: 15px; font-weight: 500; line-height: 1.3;
  }
  .rule { position: absolute; height: 2px; background: var(--orange); }
  .rule-top { left: 250px; right: 36px; top: 176px; }
  .rule-mid { left: 28px; right: 36px; top: 246px; }
  .rule-bottom { left: 28px; right: 180px; top: 310px; }
  .online {
    position: absolute; right: 36px; top: 186px;
    list-style: none; text-align: right; font-size: 16px; font-weight: 500; line-height: 1.45;
  }
  .online li, .phones li { display: flex; align-items: center; gap: 6px; }
  .online li { justify-content: flex-end; }
  .phones {
    position: absolute; left: 40px; top: 254px;
    list-style: none; font-size: 19px; font-weight: 500; line-height: 1.3;
  }
  .icon { width: 16px; height: 16px; flex: none; }
</style>
</head>
<body>
  <section class="card card-front" aria-label="Front side">
    <div class="brand-large">
      <span class="brand-dot"></span>
      <span class="brand-name">kB7</span>
    </div>
    <p class="eshop eshop-cz">www.relaxnipultiky.cz</p>
    <p class="eshop eshop-sk">www.pohodlnelavice.sk</p>
  </section>

  <section class="card card-back" aria-label="Back side">
    <div class="brand-small">
      <span class="brand-dot"></span>
      <span class="brand-name">kB7</span>
    </div>
    <div class="holder">
      <p class="holder-name">PETER KOLAR</p>
      <p class="holder-title">MSc. / CEO.</p>
    </div>
    <address class="address" style="font-style:normal">
      Borovicová 742/3,<br>
      938 05 Dunajská Streda,<br>
      Slovak republic (Slovakia)
    </address>
    <div class="rule rule-top"></div>
    <ul class="online">
      <li>info@kb7.sk
        <svg class="icon" viewBox="0 0 16 16"><rect x="1" y="3" width="14" height="10" fill="var(--orange)"/><path d="M1 3 L8 9 L15 3" fill="none" stroke="#fff" stroke-width="1.3"/></svg>
      </li>
      <li>www.kb7.sk
        <svg class="icon" viewBox="0 0 16 16" fill="none" stroke="var(--orange)" stroke-width="1.3"><circle cx="8" cy="8" r="6.5"/><ellipse cx="8" cy="8" rx="3" ry="6.5"/><path d="M1.5 8h13M2.5 5h11M2.5 11h11"/></svg>
      </li>
    </ul>
    <div class="rule rule-mid"></div>
    <ul class="phones">
      <li>
        <svg class="icon" viewBox="0 0 16 16"><path d="M3 1.5l3 3-1.5 2c1 2 2.5 3.5 4.5 4.5l2-1.5 3 3-2 2C6.5 14 2 9.5 1 3.5z" fill="var(--orange)"/></svg>
        +421 (0) 917 604 382
      </li>
      <li>
        <svg class="icon" viewBox="0 0 16 16" fill="none" stroke="var(--orange)" stroke-width="1.4"><rect x="4" y="1.5" width="8" height="13" rx="1.5"/><path d="M7 12.5h2"/></svg>
        +421 (0) 911 758 026
      </li>
    </ul>
    <div class="rule rule-bottom"></div>
  </section>
</body>
</html>
```